HUSH: Hush Until Stories Happen school library event

I need two poster designs for Hush Until Stories Happen (HUSH) in BC, requested by the PCSMG--Pacific Coast School Media Guild. One should be for elementary students and one for high school. I want the date (Monday, October 26, 2020) and Hush Until Stories Happen. I would like the posters in English and in French. French is : Ferme Ton Écran Maintenant! I'm including last year's posters as examples. I would like to be able to print the poster files on 11x17 paper.

• -The phrase "Hush Until Stories Happen" for the English version; "Ferme Ton Écran Maintenant" for the French version.
-Include the organization name: Pacific Coast School Media Guild
-The date: Monday, October 26, 2020
• I would like the elementary version to be bright and colourful--fun for younger kids. I would like the high school version to be a bit more mature for the older students. Can still be bright and colourful.

```html
<!DOCTYPE html>
<html lang="en">
<head>
<meta charset="utf-8">
<title>HUSH – Hush Until Stories Happen posters</title>
<link rel="stylesheet" href="https://fonts.googleapis.com/css2?family=Barlow+Condensed:wght@400;500;700;800&display=swap">
<style>
  :root {
    --indigo: #2f2a86;
    --sun: #f0e03a;
    --ink: #191919;
    --paper: #ebe8e3;
    --white: #ffffff;
  }
  * { margin: 0; padding: 0; box-sizing: border-box; }
  html, body { width: 1200px; height: 800px; overflow: hidden; }
  body {
    background: var(--paper);
    font-family: "Barlow Condensed", "Arial Narrow", sans-serif;
    position: relative;
  }
  .poster {
    position: absolute;
    top: 146px;
    width: 360px;
    height: 509px;
    overflow: hidden;
  }
  .poster--fr { left: 30px; background: var(--indigo); }
  .poster--hs { left: 420px; background: var(--sun); }
  .poster--en { left: 810px; background: var(--indigo); }

  .org {
    position: absolute;
    border-left: 3px solid var(--sun);
    padding: 40px 0 0 13px;
    top: 0;
    left: 219px;
    height: 89px;
    font-size: 12.5px;
    line-height: 1.25;
    font-weight: 500;
    color: var(--sun);
    width: 130px;
  }
  .poster--hs .org {
    border-left-color: var(--ink);
    color: var(--ink);
    left: 225px;
    height: 67px;
    padding-top: 13px;
    font-size: 14px;
  }

  .reader-art {
    position: absolute;
    left: 38px;
    top: 85px;
    width: 150px;
    height: 150px;
    background: var(--sun);
    border-radius: 60px 60px 8px 8px;
  }

  .headline {
    position: absolute;
    left: 49px;
    top: 240px;
    list-style: none;
  }
  .headline li {
    display: table;
    background: var(--sun);
    color: var(--indigo);
    font-weight: 700;
    font-size: 40px;
    line-height: 1;
    padding: 7px 10px 5px 8px;
    margin-bottom: 9px;
    text-transform: uppercase;
    letter-spacing: -0.5px;
  }
  .headline li.indent { margin-left: 17px; }

  .date {
    position: absolute;
    left: 49px;
    top: 442px;
    font-size: 20px;
    font-weight: 500;
    color: var(--white);
  }

  /* high school poster */
  .rule-h {
    position: absolute;
    left: 125px; right: 0; top: 134px;
    height: 8px; background: var(--ink);
  }
  .rule-v {
    position: absolute;
    left: 125px; top: 142px; bottom: 0;
    width: 8px; background: var(--ink);
  }
  .word-vertical {
    position: absolute;
    left: 32px;
    top: 300px;
    transform: rotate(-90deg);
    transform-origin: left top;
    font-size: 100px;
    font-weight: 800;
    line-height: 0.8;
    color: var(--ink);
    letter-spacing: -2px;
    white-space: nowrap;
  }
  .stack {
    position: absolute;
    left: 143px;
    top: 160px;
    font-size: 66px;
    font-weight: 700;
    line-height: 0.92;
    color: var(--ink);
    letter-spacing: -1px;
  }
  .word-big {
    position: absolute;
    left: 142px;
    top: 318px;
    font-size: 68px;
    font-weight: 800;
    line-height: 0.9;
    color: var(--ink);
    letter-spacing: -1px;
    white-space: nowrap;
  }
  .poster--hs .date {
    left: 142px;
    top: 415px;
    color: var(--ink);
    font-size: 25px;
    line-height: 1.2;
  }
</style>
</head>
<body>

  <section class="poster poster--fr" lang="fr">
    <p class="org">Pacific Coast<br>School Media<br>Guild</p>
    <div class="reader-art" role="img" aria-label="Silhouette of a child reading an open book"></div>
    <ul class="headline">
      <li>Ferme</li>
      <li class="indent">Ton Écran</li>
      <li>Maintenant</li>
    </ul>
    <p class="date">Lundi, Octobre 26, 2020</p>
  </section>

  <section class="poster poster--hs">
    <p class="org">Pacific Coast<br>School Media<br>Guild</p>
    <div class="rule-h"></div>
    <div class="rule-v"></div>
    <span class="word-vertical">HUSH</span>
    <p class="stack">UNTIL<br>STORIES</p>
    <p class="word-big">HAPPEN</p>
    <p class="date">Monday,<br>October 26, 2020</p>
  </section>

  <section class="poster poster--en">
    <p class="org">Pacific Coast<br>School Media<br>Guild</p>
    <div class="reader-art" role="img" aria-label="Silhouette of a child reading an open book"></div>
    <ul class="headline">
      <li>Hush</li>
      <li class="indent">Until Stories</li>
      <li>Happen</li>
    </ul>
    <p class="date">Monday, October 26, 2020</p>
  </section>

</body>
</html>
```